Superfoods Nutrition for Elderly

We need a thematic packaging design that fits our elderly nutrition products, that is based on our "3 Ws ethos" - eating Wisely, Widely & Wholly.

Wisely - selected superfoods and ingredients - NZ and other sources
Widely - based on the "rainbow diet" philosophy
Wholly - all natural, (no artificial flavours, colors etc). Formulated as complete meals (NOT supplementation)

Mediums:
- 400-450gram re-sealable doy packs
- 400-450gram re-sealable tin cans

Look n Feel:
Tamarewa - https://tamarewagoodness.example
Puke Nui - https://www.pukenui.example/
Harbour ledge - https://grainfieldpantry.example/collections/cereals

The name of our products may/may not be “vital mahi”. Our on-going research tells us that for the Asian market, an icon or character to personify our product may be a sound strategy. This is only for the designer to take note off.

Deliverables:
* 5 packaging designs in the range.
1x yellow + orange colored foods (star ingredient: “pure zing” – passion fruit powder)
1x red colored foods (star ingredient: (star ingredient: - Manuka honey )
1x blues/purple colored foods: (star ingredient: lorvane blackcurrant)
1 x green coloured foods (star ingredient: Green kiwi)
1 x brown/white (star ingredients: dunmore’s grass fed bone broth)

brand name, please use “VitalMahi” for now.

These will be the products:

Blue/purple: “Instant oatmeal porridge”
Ingredients: Rolled Baby Oats, Blueberries, Blackcurrant Powder, chia seeds, Blue Spirulina, Sheep’s Milk.
Star ingredient: Blackcurrant powder (support eyesight)

Brown/White: “Instant Brown Rice”
Ingredients: Organic Brown Rice, Grass fed bone broth powder, collagen peptide powder, black sesame seeds, onions and garlic powder, dried mushrooms, probiotics.
Star ingredient: Grass fed bone broth (support joint health)

Green: “Instant Smoothie”
Ingredients: Organic Green Kiwifruit, Kale powder, green apple powder, whey protein concentrate, probiotics, and sheep’s milk powder
Star ingredient: Organic green kiwi fruit(supports immunity)

Yellow/Orange “Instant Oatmeal”
Ingredients: Organic rolled baby oats, banana, organic passionfruit, apricot, dried mango, probiotics, cinnamon, sheep’s milk powder.
Star ingredient: Organic passionfruit(regulates blood glucose)

Red: “ instant amaranth cereal”
Ingredients: Organic amaranth, red apples, pomegranate, cranberries, Manuka honey powder, probiotics, sheep’s milk
Star ingredient: Manuka honey powder (anti-inflammatory)

Target Market(s)

Whose attention we are trying to grab?

Primary:
- 20 to 40 year olds buying these products for their parents/grand parents
- Health Nutrition conscious “golden agers”
Secondary
- Professional Caregivers to the elderly (homes, private hospitals etc)
- 40 year olds in the “prevention” mind set.

Font styles to use
Serif
Sans Serif

Colors

Designer to choose colors to be used in the design.

Requirements
Must have
• Mandatory:
• - clear visual que of the food color/s
• - "New Zealand" origin must come through strongly.
• - must have a blurp or feature of the star ingredient for each with mention of brand.
• e.g. for the blues+ purple, NZ blackcurrant powder for improved eyesight (cataract prevention).
• - icons for “heart health, “eyesight”, “mobility”, “gut-health”.
• - every other ingredient must be stated.
• The name of product may/may not be “vitalmahi”. Our on-going research tells us that for the Asian market, an icon or character to personify our product may be a sound strategy. This is only for the designer to take note off.
Nice to have
• Desirables:
• Ingredient origin story - e.g blackcurrant comes from Timaru etc.
• (refer to Pemberlys destination marketing…)

```html
<!DOCTYPE html>
<html lang="en">
<head>
<meta charset="utf-8">
<title>VitalMahi Instant Oatmeal Porridge – Tin Label</title>
<link rel="stylesheet" href="https://fonts.googleapis.com/css2?family=Signika:wght@700&family=Cabin:wght@400;500;600&display=swap">
<style>
  :root {
    --page-bg: #f1f1f1;
    --label-bg: #fbfbfb;
    --label-edge: #e4e4e4;
    --brand-ink: #2b2b2b;
    --purple: #6a2c91;
    --purple-line: #8a5aa8;
    --icon-grey: #b5b5b5;
    --icon-text: #8e8e8e;
    --berry-dark: #2a2438;
    --oat-tone: #c9b8a8;
  }
  * { box-sizing: border-box; margin: 0; padding: 0; }
  html, body {
    width: 1200px; height: 1200px; overflow: hidden;
    background: var(--page-bg);
  }
  .canvas { position: relative; width: 1200px; height: 1200px; }
  .label {
    position: absolute; left: 273px; top: 30px;
    width: 654px; height: 1140px;
    background: linear-gradient(90deg, var(--label-edge) 0%, var(--label-bg) 20%, var(--label-bg) 80%, var(--label-edge) 100%);
    font-family: "Cabin", sans-serif;
    color: var(--purple);
    text-align: center;
  }
  .label > * { position: absolute; left: 0; right: 0; }
  .brand {
    top: 96px;
    font-family: "Signika", sans-serif; font-weight: 700;
    font-size: 82px; letter-spacing: -1px; line-height: 1;
    color: var(--brand-ink);
  }
  .rule { height: 2px; background: var(--purple-line); left: 112px; right: 112px; }
  .rule--top { top: 192px; }
  .rule--mid { top: 368px; }
  .rule--icons-top { top: 924px; left: 108px; right: 108px; height: 1.5px; }
  .rule--icons-bottom { top: 1044px; left: 108px; right: 108px; height: 1.5px; }
  .product-name {
    top: 208px; font-size: 78px; font-weight: 500; line-height: 76px;
    letter-spacing: -1px;
  }
  .made-with { top: 382px; font-size: 24px; font-weight: 500; }
  .star-ingredient { top: 414px; font-size: 40px; font-weight: 500; }
  .benefit-pill {
    top: 462px; left: 50%; right: auto; transform: translateX(-50%);
    background: var(--purple); color: #fff;
    font-size: 24px; line-height: 30px; padding: 0 12px; border-radius: 14px;
    white-space: nowrap;
  }
  .hero-photo {
    top: 552px; left: 52px; right: 80px; height: 350px;
  }
  .benefit-icons {
    top: 938px; display: flex; justify-content: center; gap: 28px;
    left: 90px; right: 90px;
  }
  .benefit {
    width: 100px; display: flex; flex-direction: column; align-items: center;
    font-size: 16px; color: var(--icon-text);
  }
  .benefit svg { width: 64px; height: 64px; fill: var(--icon-grey); margin-bottom: 4px; }
  .net-weight { top: 1066px; font-size: 24px; }
</style>
</head>
<body>
<main class="canvas">
  <section class="label">
    <div class="brand">VitalMahi</div>
    <div class="rule rule--top"></div>
    <h1 class="product-name">Instant Oatmeal<br>Porridge</h1>
    <div class="rule rule--mid"></div>
    <p class="made-with">Made With</p>
    <p class="star-ingredient">Lorvane Blackcurrant</p>
    <p class="benefit-pill">Supports Eyesight</p>

    <svg class="hero-photo" viewBox="0 0 522 350" role="img" aria-label="Photo of a white bowl of oatmeal porridge flanked by clusters of blackcurrants">
      <defs>
        <radialGradient id="oatFill" cx="50%" cy="45%" r="55%">
          <stop offset="0%" stop-color="#ddd0c3"/>
          <stop offset="100%" stop-color="var(--oat-tone)"/>
        </radialGradient>
        <radialGradient id="berryFill" cx="40%" cy="40%" r="60%">
          <stop offset="0%" stop-color="#4a4060"/>
          <stop offset="100%" stop-color="var(--berry-dark)"/>
        </radialGradient>
      </defs>
      <ellipse cx="70" cy="150" rx="62" ry="120" fill="url(#berryFill)"/>
      <ellipse cx="460" cy="230" rx="50" ry="95" fill="url(#berryFill)"/>
      <circle cx="282" cy="174" r="174" fill="#ffffff"/>
      <circle cx="282" cy="174" r="155" fill="url(#oatFill)"/>
    </svg>

    <div class="rule rule--icons-top"></div>
    <div class="benefit-icons">
      <div class="benefit">
        <svg viewBox="0 0 64 64" aria-hidden="true"><path d="M32 56 C10 40 4 30 4 20 A14 14 0 0 1 32 14 A14 14 0 0 1 60 20 C60 30 54 40 32 56Z"/></svg>
        Heart Health
      </div>
      <div class="benefit">
        <svg viewBox="0 0 64 64" aria-hidden="true"><path d="M2 32 C14 16 50 16 62 32 C50 48 14 48 2 32Z M32 21 A11 11 0 1 0 32 43 A11 11 0 1 0 32 21Z" fill-rule="evenodd"/><circle cx="32" cy="32" r="6"/></svg>
        Eyesight
      </div>
      <div class="benefit">
        <svg viewBox="0 0 64 64" aria-hidden="true"><path d="M8 38 H40 V28 L58 42 L40 56 V46 H8Z"/><rect x="8" y="20" width="22" height="5" rx="2"/><rect x="14" y="10" width="16" height="5" rx="2"/></svg>
        Mobility
      </div>
      <div class="benefit">
        <svg viewBox="0 0 64 64" aria-hidden="true"><path d="M32 6 A26 26 0 1 0 32 58 A26 26 0 1 0 32 6Z M32 11 A21 21 0 1 1 32 53 A21 21 0 1 1 32 11Z" fill-rule="evenodd"/><rect x="29" y="20" width="6" height="24" rx="2"/><rect x="20" y="29" width="24" height="6" rx="2"/></svg>
        Gut-Health
      </div>
    </div>
    <div class="rule rule--icons-bottom"></div>
    <p class="net-weight">Net weight: 450g</p>
  </section>
</main>
</body>
</html>
```